Need a design for Loan Site with new age design

We need a design for our site www.fernpivot.in , we deal with different verticals like home loan, personal loan, loan against property and business loans. Feel free to get in touch if you have any questions.

I have like the concept of the drop down on the eye level where consumer is able to select the product they wish and continue with the form https://www.tallowcrest.com/ . They are in the same line of business as we are.

Here are few more designs which i personally like just to get idea about the taste

https://plumweatherly.com/
http://vexlar.com/partners

Industry/Entity Type

Loan

Number of Pages Required

2 page

Colors
34a7d7
add136
faa54b
fbee3e

Requirements
Must have
• I have like the concept of the drop down on the eye level where consumer is able to select the product they wish and continue with the form https://www.tallowcrest.com/ . They are in the same line of business as we are.
• Here are few more designs which i personally like just to get idea about the taste
• https://plumweatherly.com/
• http://vexlar.com/partners

```html
<!DOCTYPE html>
<html lang="en">
<head>
<meta charset="utf-8">
<title>Fern Pivot – Loans</title>
<link href="https://fonts.googleapis.com/css2?family=Open+Sans:wght@400;600;700;800&display=swap" rel="stylesheet">
<style>
:root{
  --blue:#34a7d7;
  --blue-dark:#1f7fae;
  --navy:#17537a;
  --green:#add136;
  --green-btn:#2fb34a;
  --orange:#faa54b;
  --yellow:#fbee3e;
  --ink:#333b44;
  --muted:#7b848c;
  --light:#f1f3f5;
  --white:#ffffff;
}
*{box-sizing:border-box;margin:0;padding:0}
html,body{width:1200px;height:2500px;overflow:hidden}
body{font-family:"Open Sans",Arial,sans-serif;color:var(--ink);background:var(--white);position:relative}
.abs{position:absolute}

/* header */
.site-header{position:absolute;top:0;left:0;width:1200px;height:78px;z-index:3;display:flex;align-items:center;justify-content:space-between;padding:0 96px}
.brand{display:flex;align-items:center;gap:10px;color:var(--white);font-weight:700;font-size:22px}
.brand-mark{width:26px;height:26px;background:var(--blue);border-radius:4px}
.main-nav{display:flex;height:78px}
.main-nav a{color:var(--white);text-decoration:none;font-size:14px;padding:0 18px;display:flex;align-items:center}
.main-nav a.active{background:var(--blue)}

/* hero */
.hero{position:absolute;top:0;left:0;width:1200px;height:590px;background:linear-gradient(180deg,#5f7f97 0%,#8ea6b6 45%,#b9a98a 100%)}
.hero-photo{position:absolute;inset:0;background:linear-gradient(90deg,rgba(120,100,70,.55) 0%,rgba(150,170,185,.2) 40%,rgba(150,170,185,.1) 65%,rgba(140,115,80,.55) 100%)}
.hero-title{position:absolute;top:128px;width:100%;text-align:center;color:var(--white);font-size:40px;font-weight:600}
.hero-sub{position:absolute;top:182px;width:100%;text-align:center;color:var(--white);font-size:22px}
.finder{position:absolute;top:226px;left:348px;display:flex;height:44px}
.finder .field{background:var(--white);border:1px solid #ccd;width:210px;padding:0 12px;display:flex;align-items:center;font-size:14px;color:var(--muted)}
.finder .select{justify-content:space-between;width:210px}
.finder .btn-search{background:var(--green-btn);color:var(--white);width:80px;display:flex;align-items:center;justify-content:center;font-size:14px;font-weight:600}
.product-menu{position:absolute;top:270px;left:558px;width:420px;background:var(--white);display:grid;grid-template-columns:1fr 1fr;box-shadow:0 4px 10px rgba(0,0,0,.25)}
.product-menu span{font-size:14px;padding:9px 14px;border-bottom:1px solid #e4e7ea;border-right:1px solid #e4e7ea}
.product-menu span.hover{background:#e4eef5}

/* who we are */
.section-title{text-align:center;font-weight:700;font-size:24px;color:var(--navy)}
.section-sub{text-align:center;font-size:14px;color:var(--muted)}
.who{position:absolute;top:600px;left:0;width:1200px;height:330px}
.who .section-title{margin-top:14px}
.who .section-sub{margin-top:6px}
.who-photo{position:absolute;top:82px;left:222px;width:280px;height:200px;background:linear-gradient(135deg,#d8c7a8,#a88a5c 60%,#6d5838)}
.who-text{position:absolute;top:80px;left:525px;width:455px;font-size:13px;line-height:22px;color:var(--muted)}
.btn-green{background:var(--green-btn);color:var(--white);font-size:15px;font-weight:600;display:inline-flex;align-items:center;justify-content:center}
.who .btn-green{position:absolute;top:232px;left:368px;width:166px;height:46px}

/* partners */
.partners{position:absolute;top:940px;left:0;width:1200px;height:160px;border-top:1px solid #e1e4e7;border-bottom:1px solid #e1e4e7}
.partners .section-title{margin-top:30px;font-size:26px}
.partner-row{position:absolute;top:100px;left:150px;width:900px;display:flex;justify-content:space-between;align-items:center}
.partner{font-size:20px;font-weight:700;color:#b3282d}
.partner.alt{color:var(--navy)}

/* features */
.features{position:absolute;top:1115px;left:0;width:1200px;height:430px;background:linear-gradient(180deg,#2a9ad0,#1f78ad)}
.features .section-title{color:var(--white);margin-top:30px;font-size:26px}
.features .section-sub{color:var(--white);font-size:22px;font-weight:600}
.feature-figure{position:absolute;top:130px;left:520px;width:160px;height:250px;border-radius:80px 80px 0 0;background:linear-gradient(180deg,#fcd9a8,#2f3e4c 45%,#1c2835)}
.feature{position:absolute;width:330px;color:var(--white)}
.feature h3{font-size:15px;font-weight:700;color:var(--white);text-transform:uppercase}
.feature p{font-size:11px;line-height:17px;margin-top:6px;opacity:.85}
.feature.left{left:150px;text-align:right}
.feature.right{left:720px}
.f-icon{position:absolute;width:42px;height:42px;background:var(--white);border-radius:4px;display:flex;align-items:center;justify-content:center}

/* posts */
.posts{position:absolute;top:1545px;left:0;width:1200px;height:660px;background:var(--light)}
.posts .section-title{margin-top:42px;font-size:26px;color:var(--ink)}
.dots{display:flex;gap:8px;justify-content:center;margin-top:10px}
.dots i{width:10px;height:10px;border-radius:50%;background:#bcc3c9}
.dots i.on{background:var(--muted)}
.post{position:absolute;top:125px;width:372px;height:420px;overflow:hidden}
.post-photo{position:absolute;inset:0}
.post h4{position:absolute;left:16px;right:16px;top:235px;color:var(--white);font-size:17px;font-weight:800;text-transform:uppercase}
.post p{position:absolute;left:16px;right:16px;top:285px;color:var(--white);font-size:11px;line-height:17px}
.read-more{position:absolute;right:0;bottom:0;background:var(--blue);color:var(--white);font-size:11px;padding:6px 12px}
.posts .btn-green{position:absolute;top:595px;left:540px;width:120px;height:42px;font-size:14px}

/* cta */
.tagline{position:absolute;top:2222px;width:100%;text-align:center;font-size:19px;color:#a7adb3;letter-spacing:.5px}
.cta{position:absolute;top:2270px;left:0;width:1200px;height:190px;background:linear-gradient(180deg,#7fc9e8,#b9e3f3)}
.cta-box{position:absolute;top:20px;left:440px;width:320px;height:60px;background:var(--blue);color:var(--white);font-size:24px;font-weight:600;display:flex;align-items:center;justify-content:center}
.cta .btn-green{position:absolute;top:100px;left:525px;width:150px;height:48px;font-size:20px}
.site-footer{position:absolute;top:2460px;left:0;width:1200px;height:40px;background:var(--navy);display:flex;align-items:center;justify-content:space-between;padding:0 96px;color:#cfe1ec;font-size:11px}
.site-footer nav{display:flex;gap:22px}
</style>
</head>
<body>

<section class="hero">
  <div class="hero-photo" role="img" aria-label="Stacks of coins in soft focus on a desk"></div>
  <h1 class="hero-title">Looking For a Secured Or Unsecured Loan?</h1>
  <p class="hero-sub">We will help you get Best Interest Rates</p>
  <div class="finder">
    <div class="field">I would like to</div>
    <div class="field select">Select a Product
      <svg width="10" height="6"><path d="M0 0h10L5 6z" fill="#777"/></svg>
    </div>
    <div class="btn-search">Search</div>
  </div>
  <div class="product-menu">
    <span>Home Loan</span><span>Savings Account</span>
    <span class="hover">Personal Loan</span><span>Debit Card</span>
    <span>Business Loan</span><span>Car Insurance</span>
    <span>Loan against Property</span><span>Life Insurance</span>
    <span>Car Loan</span><span>Health Insurance</span>
  </div>
</section>

<header class="site-header">
  <div class="brand"><span class="brand-mark"></span>Fern Pivot</div>
  <nav class="main-nav">
    <a class="active" href="#">Home</a><a href="#">Who we are</a><a href="#">Lenders</a><a href="#">Blog</a><a href="#">Careers</a><a href="#">Contact us</a>
  </nav>
</header>

<section class="who">
  <h2 class="section-title">WHO WE ARE</h2>
  <p class="section-sub">We will help you get Best Interest Rate, We are Best Choice For You</p>
  <div class="who-photo" role="img" aria-label="Model house on a stack of banknotes"></div>
  <p class="who-text">We compare loans from trusted lenders so you can choose with confidence. Our team reviews rates, fees and terms across home loans, personal loans, business loans and loans against property. Tell us what you need and we match you with offers that suit your income and goals. The process is simple, quick and fully transparent, with friendly experts ready to guide you at every step until your loan is approved and paid out.</p>
  <span class="btn-green">View Our Career</span>
</section>

<section class="partners">
  <h2 class="section-title">WE WORK WITH ALL PREMIUM FINANCIAL INSTITUTIONS</h2>
  <div class="partner-row">
    <span class="partner">Harborline Bank</span>
    <span class="partner">Meridia Bank</span>
    <span class="partner alt">Crestmont Bank</span>
    <span class="partner alt">Sundara Finserv</span>
    <span class="partner alt">Kestrel Bank</span>
  </div>
</section>

<section class="features">
  <h2 class="section-title">OUR FEATURES</h2>
  <p class="section-sub">Bring best services for you</p>
  <div class="feature-figure" role="img" aria-label="Illustrated businessman in a suit"></div>

  <div class="feature left" style="top:150px">
    <h3>Get approval<br>within 7 business days</h3>
    <p>Quick checks and clear steps mean most applicants receive a decision within one working week.</p>
  </div>
  <div class="f-icon" style="top:165px;left:500px">
    <svg width="22" height="22"><path d="M3 11l6 6L19 5" stroke="#1f78ad" stroke-width="3" fill="none"/></svg>
  </div>
  <div class="feature left" style="top:275px">
    <h3>Compare quotes<br>from all major financial institutions</h3>
    <p>See offers side by side and pick the rate, tenure and fee that works best for you.</p>
  </div>
  <div class="f-icon" style="top:290px;left:500px">
    <svg width="22" height="22"><rect x="3" y="10" width="4" height="9" fill="#1f78ad"/><rect x="9" y="5" width="4" height="14" fill="#1f78ad"/><rect x="15" y="8" width="4" height="11" fill="#1f78ad"/></svg>
  </div>

  <div class="feature right" style="top:150px">
    <h3>Doorstep deliveries</h3>
    <p>Our agents collect your papers at home or office, at a time that suits your schedule.</p>
  </div>
  <div class="f-icon" style="top:150px;left:658px">
    <svg width="22" height="22"><path d="M3 11L11 4l8 7v8H3z" fill="#1f78ad"/></svg>
  </div>
  <div class="feature right" style="top:275px">
    <h3>Easy documentation</h3>
    <p>Only a few basic documents are needed, and we help you check each one before submission.</p>
  </div>
  <div class="f-icon" style="top:275px;left:658px">
    <svg width="22" height="22"><path d="M5 2h9l4 4v14H5z" fill="#1f78ad"/></svg>
  </div>
</section>

<section class="posts">
  <h2 class="section-title">LATEST POSTS</h2>
  <div class="dots"><i></i><i class="on"></i><i></i></div>
  <article class="post" style="left:222px">
    <div class="post-photo" role="img" aria-label="Happy family outdoors under a blue sky" style="background:linear-gradient(180deg,#6fa8d6,#4b7fa8 55%,#2d4f6a)"></div>
    <h4>Awesome long blog title here</h4>
    <p>Simple tips to plan your budget, improve your credit score and choose the right loan for your family.</p>
    <span class="read-more">Read more</span>
  </article>
  <article class="post" style="left:606px">
    <div class="post-photo" role="img" aria-label="Stacks of coins with a small plant" style="background:linear-gradient(180deg,#b99568,#7d5c3a 55%,#3e2e1f)"></div>
    <h4>Amazing long and long blog title here</h4>
    <p>How interest rates work, what affects them and how to compare offers before you sign.</p>
    <span class="read-more">Read more</span>
  </article>
  <span class="btn-green">VIEW ALL</span>
</section>

<p class="tagline">"WE WILL HELP YOU GET BEST INTEREST RATE, WE ARE BEST CHOICE FOR YOU"</p>

<section class="cta" role="img" aria-label="Light blue city skyline with houses and a car">
  <div class="cta-box">What Are You Waiting For?</div>
  <span class="btn-green">Inquire now</span>
</section>

<footer class="site-footer">
  <nav><span>Home</span><span>Who we are</span><span>Lenders</span><span>Blog</span><span>Careers</span><span>Contact Us</span></nav>
  <span>Copyright © Fern Pivot. All Rights Reserved.</span>
</footer>

</body>
</html>
```